Brell Harbor Company Business Cards

Front and Back Business Card - logo and text setup - cool design. I need workable photoshop or illustrator files so I can setup each employee card with design that is created
Updates

Hi everyone, thank you for the great entries. Please no more white and blue cards - there are so many already - black and silver only now please. thanks!

Target Market(s)

Construction Industry - Facility Managers

Industry/Entity Type

Construction

Contact Information for Business Card

I really like contemporary simplistic looks - clean neat....not opposed to seeing some black backrounds

Requirements
Must have
• Logo/website address with design on front only - www.brellharbor-example.com (logo attached)
• Back:
• Name/Title/Company Address/Phone/email address
Nice to have
• Cool design
Should not have
• Nothing gimmicky like Fire or Water - since we are a Fire Protection company - it has all been done

```html
<!DOCTYPE html>
<html lang="en">
<head>
<meta charset="utf-8">
<title>Brell Harbor Company – Business Cards</title>
<link href="https://fonts.googleapis.com/css2?family=Roboto:wght@300;400;700;900&display=swap" rel="stylesheet">
<style>
  :root {
    --page-bg: #d4d4d4;
    --card-dark: #0b0c16;
    --card-navy: #121526;
    --magenta: #6e0a5c;
    --magenta-deep: #3a0630;
    --accent: #e8553e;
    --text-light: #e4e4ea;
    --text-muted: #a9a9b6;
  }
  * { margin: 0; padding: 0; box-sizing: border-box; }
  html, body { width: 1200px; height: 1200px; overflow: hidden; }
  body {
    background: var(--page-bg);
    font-family: "Roboto", Arial, sans-serif;
    position: relative;
  }
  .card {
    position: absolute;
    left: 150px;
    width: 900px;
    height: 514px;
    background: linear-gradient(135deg, var(--card-navy) 0%, var(--card-dark) 60%);
    overflow: hidden;
  }
  .card--front { top: 60px; }
  .card--back { top: 626px; }
  .card__art { position: absolute; inset: 0; width: 100%; height: 100%; }

  /* front */
  .front__website {
    position: absolute;
    left: 60px; top: 52px;
    font-size: 22px; font-weight: 300;
    color: var(--text-muted);
    letter-spacing: 0.5px;
  }
  .front__name {
    position: absolute;
    right: 110px; top: 290px;
    font-size: 58px; font-weight: 700;
    color: var(--accent);
    letter-spacing: 1px;
  }

  /* back */
  .back__identity { position: absolute; left: 72px; top: 80px; color: var(--text-light); }
  .back__name { font-size: 40px; font-weight: 300; letter-spacing: 1px; }
  .back__name strong { font-weight: 900; }
  .back__position { font-size: 16px; color: var(--text-muted); margin-top: 4px; }

  .back__brand { position: absolute; right: 92px; top: 222px; text-align: right; }
  .back__brand-name { font-size: 26px; font-weight: 700; color: var(--accent); }
  .back__brand-url { font-size: 11px; color: var(--text-muted); margin-top: 3px; }

  .contact-list {
    position: absolute;
    right: 60px; bottom: 46px;
    list-style: none;
    display: flex; flex-direction: column; gap: 16px;
    align-items: flex-end;
  }
  .contact-list__item {
    display: flex; align-items: center; gap: 14px;
    font-size: 15px; color: var(--text-light);
  }
  .contact-list__icon { width: 26px; height: 26px; }
</style>
</head>
<body>

<section class="card card--front" aria-label="Card front">
  <svg class="card__art" viewBox="0 0 900 514" preserveAspectRatio="none" aria-hidden="true">
    <defs>
      <radialGradient id="frontGlow" cx="0.85" cy="1" r="0.9">
        <stop offset="0" stop-color="#5a0840"/>
        <stop offset="0.55" stop-color="#26061f"/>
        <stop offset="1" stop-color="#0b0c16"/>
      </radialGradient>
    </defs>
    <path d="M140 180 Q150 140 200 150 L860 260 Q900 268 900 310 L900 514 L60 514 Z"
          fill="url(#frontGlow)" stroke="#1a1c30" stroke-width="2"/>
  </svg>
  <p class="front__website">www.brellharbor-example.com</p>
  <p class="front__name">Brell Harbor</p>
</section>

<section class="card card--back" aria-label="Card back">
  <svg class="card__art" viewBox="0 0 900 514" preserveAspectRatio="none" aria-hidden="true">
    <defs>
      <radialGradient id="backGlow" cx="0.15" cy="0.3" r="0.85">
        <stop offset="0" stop-color="#7a0c65"/>
        <stop offset="0.5" stop-color="#3a0630"/>
        <stop offset="1" stop-color="#120818"/>
      </radialGradient>
    </defs>
    <path d="M0 0 L900 0 L900 210 Q900 270 840 270 L60 290 Q20 290 20 250 L20 120 Q20 60 0 40 Z"
          fill="url(#backGlow)"/>
  </svg>

  <div class="back__identity">
    <p class="back__name"><strong>YOUR</strong> Name</p>
    <p class="back__position">Position</p>
  </div>

  <div class="back__brand">
    <p class="back__brand-name">Brell Harbor</p>
    <p class="back__brand-url">www.brellharbor-example.com</p>
  </div>

  <ul class="contact-list">
    <li class="contact-list__item">Phone
      <svg class="contact-list__icon" viewBox="0 0 26 26" aria-hidden="true">
        <circle cx="13" cy="13" r="11.5" fill="none" stroke="var(--accent)" stroke-width="1.6"/>
        <path d="M9 8 Q8 13 12 17 Q15 19 18 18 L16.5 15.5 L14.5 16 Q11.5 14 10.5 11 L11 9.5 Z" fill="var(--accent)"/>
      </svg>
    </li>
    <li class="contact-list__item">email
      <svg class="contact-list__icon" viewBox="0 0 26 26" aria-hidden="true">
        <circle cx="13" cy="13" r="11.5" fill="none" stroke="var(--accent)" stroke-width="1.6"/>
        <rect x="7.5" y="9" width="11" height="8" fill="none" stroke="var(--accent)" stroke-width="1.5"/>
        <path d="M7.5 9 L13 13.5 L18.5 9" fill="none" stroke="var(--accent)" stroke-width="1.5"/>
      </svg>
    </li>
    <li class="contact-list__item">Address
      <svg class="contact-list__icon" viewBox="0 0 26 26" aria-hidden="true">
        <circle cx="13" cy="13" r="11.5" fill="none" stroke="var(--accent)" stroke-width="1.6"/>
        <path d="M13 19.5 Q8.5 14 8.5 11.5 A4.5 4.5 0 0 1 17.5 11.5 Q17.5 14 13 19.5 Z" fill="var(--accent)"/>
        <circle cx="13" cy="11.5" r="1.7" fill="var(--card-dark)"/>
      </svg>
    </li>
  </ul>
</section>

</body>
</html>
```